Ready to be wowed! Snazzy, sassy, classy Realtor seeking Web banner for unique innovative Realtor!

Placer County Realtor need web banner re-design. Looking for classy, classic, clean design appealing to elite prospects. Previous focus was short sales now looking to gear towards listing and selling homes, remove short sale focus. Must include, license # 04729318, HR logo, phone, email, etc. check out LiaPorter.com for reference info. I am open to suggestions for other needed content for THE BEST WEB BANNER ON EARTH! LOL. I really want to appeal to the upscale clients, also will be getting away from orange colors going more to a green. Please contact me at LiaPorterSells@mailvista.com for more info
measurements of banner; Images of exactly 960 × 120 pixels will be used as-is. It's Wordpress Genesis.
Updates

I'm really looking for something clean that looks upscale and luxury, classy. 

Please update email address to lia@liaporter.com

Reason: I still haven't gotten what I want. I noticed some really good designs closer to the end here, I'm hoping to allow those folks and maybe a few new ones the opportunity to give me exactly what I want! Thanks!

Reason: I still don't have what I want. I want a simple design that shows that I am a Realtor, maybe a picture of a house???? or something related to real estate. Less emphasis on the Halverson Realty logo. Classy and upscale. Fonts should be easy to read but not so simply boring. Please, please, please read the brief!! I REALLY want a good banner!!

Please take a look at the site color adjustment. That's what color it will stay. www.LiaPorter.com

Reason: I'm ready to move this to the end now. I need a design. I'm extending hopefully only this last time to take a vote on them. I will be reaching out to a few select designers to make a few modifications. I appreciate everyone's time on this as you know this is a very tough and important decision to make.

Reason: Need more input

Reason: still trying to decide

Target Market(s)

upscale home sellers

Industry/Entity Type

Realtor

Requirements
Must have
• License # 04729318
Phone (555)304-2871
HR LOGO (attached)
areas of service- Roseville, Rocklin, Granite Bay
LiaPorterSells@mailvista.com

```html
<!DOCTYPE html>
<html lang="en">
<head>
<meta charset="utf-8">
<title>Lia Porter – Realtor Banner</title>
<link rel="stylesheet" href="https://fonts.googleapis.com/css2?family=Cormorant+Garamond:ital,wght@1,700&family=Open+Sans:wght@400;600;700&display=swap">
<style>
  :root {
    --leaf: #a8c15c;
    --leaf-text: #a3bd55;
    --navy: #2b3b8f;
    --frame: #c9c9c9;
    --white: #ffffff;
    --license: #6f7a4a;
    --portrait-a: #c79a62;
    --portrait-b: #f1d9b8;
  }
  html, body {
    margin: 0;
    padding: 0;
    width: 1200px;
    height: 207px;
    overflow: hidden;
    background: var(--white);
  }
  .banner {
    position: relative;
    width: 1200px;
    height: 207px;
    font-family: "Open Sans", Arial, sans-serif;
  }
  .banner-frame {
    position: absolute;
    left: 8px;
    top: 27px;
    width: 1182px;
    height: 146px;
    border: 1px solid var(--frame);
    box-sizing: border-box;
  }
  .agent-panel {
    position: absolute;
    left: 0;
    top: 0;
  }
  .agent-portrait {
    position: absolute;
    left: 11px;
    top: 30px;
    width: 140px;
    height: 141px;
    background: linear-gradient(160deg, var(--portrait-b) 0%, var(--portrait-a) 100%);
  }
  .agent-name {
    position: absolute;
    left: 226px;
    top: 36px;
    margin: 0;
    font-family: "Cormorant Garamond", Georgia, serif;
    font-style: italic;
    font-weight: 700;
    font-size: 76px;
    line-height: 1;
    color: var(--navy);
    letter-spacing: 3px;
    white-space: nowrap;
  }
  .agent-title {
    position: absolute;
    left: 172px;
    top: 117px;
    margin: 0;
    font-weight: 700;
    font-size: 21.3px;
    color: var(--white);
    white-space: nowrap;
  }
  .agent-license {
    position: absolute;
    left: 552px;
    top: 150px;
    font-size: 11px;
    color: var(--license);
  }
  .contact-line {
    position: absolute;
    left: 736px;
    top: 33px;
    margin: 0;
    font-weight: 700;
    font-size: 29.5px;
    color: var(--leaf-text);
    white-space: nowrap;
  }
  .contact-email {
    position: absolute;
    left: 738px;
    top: 78px;
    margin: 0;
    font-weight: 600;
    font-size: 16px;
    color: var(--navy);
    white-space: nowrap;
  }
  .service-area {
    position: absolute;
    right: 255px;
    top: 107px;
    margin: 0;
    text-align: right;
    font-weight: 400;
    font-size: 26px;
    line-height: 34px;
    color: var(--leaf-text);
    white-space: nowrap;
  }
  .brokerage-name {
    position: absolute;
    left: 966px;
    top: 76px;
    width: 214px;
    height: 94px;
    display: flex;
    align-items: center;
    justify-content: center;
    font-weight: 700;
    font-size: 24px;
    color: var(--navy);
    white-space: nowrap;
  }
</style>
</head>
<body>
<div class="banner">
  <div class="banner-frame"></div>

  <svg class="agent-panel" width="700" height="207" viewBox="0 0 700 207" aria-hidden="true">
    <polygon points="9,28.5 620,28.5 696,100 620,171.5 9,171.5" fill="var(--leaf)" stroke="var(--navy)" stroke-width="3"/>
  </svg>

  <div class="agent-portrait" role="img" aria-label="Portrait photo of the agent"></div>

  <h1 class="agent-name">Lia Porter</h1>
  <p class="agent-title">EXPERIENCED LISTING AND SELLING AGENT</p>
  <span class="agent-license">#04729318</span>

  <p class="contact-line">Call or Text 555.304.2871</p>
  <p class="contact-email">lia@liaporter.com</p>
  <p class="service-area">Servicing Roseville<br>Rocklin &amp; Granite Bay</p>

  <div class="brokerage-name">Halverson Realty</div>
</div>
</body>
</html>
```